REDESIGN COUPLE PAGES FOR SURGE VIDEO ADS

PLEASE REDESIGN THIS PAGE FOR ME:
http://pagekitfinder.com/rk/milo/surge/pricing.html
I need it to be easy to read for the end user so the customer knows exactly what he will be getting. Make an emphasis on the subscription as the most popular item....and also the price per video format should be emphasized too.

Target Market(s)

B2B

Industry/Entity Type

Video Production

Number of Pages Required

3 page

Colors

Designer to choose colors to be used in the design.

Requirements
Must have
• PLEASE REDESIGN THIS PAGE FOR ME:
• http://pagekitfinder.com/rk/milo/surge/pricing.html
• I need it to be easy to read for the end user so the customer knows exactly what he will be getting. Make an emphasis on the subscription as the most popular item....and also the price per video format should be emphasized too.
Nice to have
Should not have

```html
<!DOCTYPE html>
<html lang="en">
<head>
<meta charset="utf-8">
<title>Surge Pricing</title>
<link rel="stylesheet" href="https://fonts.googleapis.com/css2?family=Lato:wght@400;700;900&display=swap">
<style>
:root{
  --navy:#161e2e;
  --navy-2:#1d2740;
  --blue:#3b63da;
  --blue-2:#5f8af0;
  --blue-soft:#c9daf8;
  --sub-body:#eef4ff;
  --accent:#e8573a;
  --line:#9aa0aa;
  --text:#1a1a1a;
  --white:#ffffff;
  --link:#4d7cf0;
}
*{box-sizing:border-box;margin:0;padding:0}
html,body{width:776px;height:1200px;overflow:hidden;background:var(--white);font-family:'Lato',sans-serif;color:var(--text)}
.page{position:relative;width:776px;height:1200px}

.site-header{position:absolute;left:0;top:0;width:776px;height:62px;background:var(--navy)}
.brand{position:absolute;left:85px;top:17px;color:var(--white)}
.brand-name{font-weight:900;font-size:17px;letter-spacing:3px;line-height:17px;display:block}
.brand-tag{font-weight:700;font-size:5.6px;letter-spacing:.9px;display:block;margin-top:3px;color:#d7dbe3}
.main-nav{position:absolute;left:254px;top:25px;display:flex;gap:9px;font-size:9.3px;color:var(--white)}
.main-nav .active{color:var(--link)}
.login{position:absolute;left:607px;top:25px;font-size:9.3px;color:var(--white)}
.signup{position:absolute;left:639px;top:18px;width:52px;height:26px;border-radius:2px;background:linear-gradient(90deg,var(--blue),var(--blue-2));color:var(--white);font-size:9.3px;display:flex;align-items:center;justify-content:center}

.page-title{position:absolute;top:92px;left:0;width:776px;text-align:center;font-weight:900;font-size:15.5px;letter-spacing:-.2px}

.pricing{position:absolute;left:85px;top:140px;display:flex;height:783px}
.plan{width:101px;position:relative;border-right:1px solid #d5d9df}
.plan:first-child{border-left:1px solid #d5d9df}
.plan-head{height:51px;background:linear-gradient(180deg,var(--blue),var(--blue-2));color:var(--white);text-align:center;padding-top:9px}
.plan-name{font-weight:900;font-size:10.3px;display:block}
.plan-sub{font-weight:900;font-size:6.6px;line-height:7px;display:block;margin-top:5px;color:#dfe8ff;padding:0 4px}
.plan-price{height:51px;background:var(--blue-soft);text-align:center;padding-top:8px;font-size:7px;border-bottom:2px solid var(--accent)}
.plan-price strong{display:block;font-size:13.5px;font-weight:900;line-height:15px}
.plan--featured .plan-head{background:var(--navy)}
.plan--featured .plan-sub{padding:0 14px}
.plan--featured .plan-price{background:var(--navy);color:var(--white)}
.plan--featured{background:var(--sub-body)}
.features-head{height:102px;background:var(--navy);color:var(--white);font-weight:900;font-size:12.5px;display:flex;align-items:center;justify-content:center;border-bottom:2px solid var(--accent)}
.row{height:26px;margin:0 7px;border-bottom:1px solid var(--line);font-size:5.6px;display:flex;align-items:center;padding-left:1px;text-transform:uppercase}
.row.keep{text-transform:none}
.calc{height:26px;margin:0 7px;border-bottom:1px solid var(--line);font-size:6px;display:flex;align-items:center;justify-content:space-between;padding:0 4px 0 2px}
.calc.grand{font-weight:900}
.qty{height:26px;margin:0 7px;border-bottom:1px solid var(--line);display:flex;align-items:center;justify-content:center}
.qty span{width:10px;height:9px;border:1px solid #9fb3d8;font-size:5.5px;display:flex;align-items:center;justify-content:center;background:var(--white)}
.buy{display:flex;align-items:center;justify-content:center;width:52px;height:18px;margin:7px 0 0 7px;border-radius:2px;background:linear-gradient(90deg,var(--blue),var(--blue-2));color:var(--white);font-size:6px;font-weight:900}

.site-footer{position:absolute;left:0;top:993px;width:776px;height:207px;background:var(--navy);color:var(--white)}
.footer-brand{position:absolute;left:85px;top:42px}
.footer-brand .brand-name{font-size:23px;line-height:23px;letter-spacing:4px}
.footer-brand .brand-tag{font-size:8px;letter-spacing:1.3px;margin-top:4px}
.footer-tagline{position:absolute;left:85px;top:93px;font-weight:900;font-size:9.3px}
.footer-col-title{position:absolute;font-weight:900;font-size:12px}
.quick-title{left:346px;top:40px}
.about-title{left:484px;top:40px;font-size:10.5px}
.about-title::after{content:"";position:absolute;left:0;top:21px;width:26px;height:1px;background:#8a93a6}
.quick-links{position:absolute;left:346px;top:86px;list-style:none;font-weight:900;font-size:10.3px;line-height:18.6px}
.about-text{position:absolute;left:484px;top:95px;width:210px;font-weight:900;font-size:10.3px;line-height:12.5px}
.social{position:absolute;left:483px;top:148px;display:flex;gap:6px}
.social span{width:20px;height:20px;border-radius:50%;background:#2a3447}
</style>
</head>
<body>
<div class="page">
  <header class="site-header">
    <div class="brand"><span class="brand-name">SURGE</span><span class="brand-tag">MARKETING VIDEOS MADE FOR YOU</span></div>
    <nav class="main-nav"><span>Home</span><span>How It Works</span><span>Examples</span><span>FAQ</span><span>Contact Us</span><span class="active">Pricing</span><span>Calendar</span></nav>
    <span class="login">Log In</span>
    <span class="signup">Sign Up</span>
  </header>

  <h1 class="page-title">NO HIDDEN CHARGES! CHOOSE YOUR DEAL!</h1>

  <section class="pricing">
    <div class="plan">
      <div class="features-head">FEATURES</div>
      <div class="row">Videos included</div><div class="row">Cost per video format</div><div class="row">Delivery speed</div><div class="row">Revisions</div><div class="row">Final file formats</div><div class="row">Wide screen video format</div><div class="row">Large square video format</div><div class="row">Vertical video format</div><div class="row">Page cover video format</div><div class="row">Holiday theme video</div><div class="row">Seasonal theme video</div><div class="row">Content done for you</div><div class="row">Full branding in video</div><div class="row">Full copyright ownership</div><div class="row">Full reselling rights</div><div class="row">Premium video clips</div><div class="row">Use my images</div><div class="row">Use my video footage</div><div class="row">Use my background music</div><div class="row">Fully licensed<br>background music</div>
    </div>

    <div class="plan">
      <div class="plan-head"><span class="plan-name">AL A CARTE</span><span class="plan-sub">AS NEEDED BASIS</span></div>
      <div class="plan-price">STARTS AT ONLY<strong>$37.00</strong>VIDEO FORMAT</div>
      <div class="row">Custom</div><div class="row keep">Starts @ $37/video</div><div class="row">24 hours</div><div class="row">Unlimited</div><div class="row keep">Mp4 FULL HD 1080P</div><div class="row">Included</div><div class="row">Included</div><div class="row">Included</div><div class="row">Included</div><div class="row">Optional</div><div class="row">Optional</div><div class="row">Included</div><div class="row">Included</div><div class="row">Included</div><div class="row">Included</div><div class="row">Included</div><div class="row">Included</div><div class="row">Included</div><div class="row">Included</div><div class="row">Included</div>
      <div class="qty"><span>-</span><span>1</span><span>+</span></div>
      <div class="calc"><span>Total</span><span>$149</span></div>
      <div class="calc"><span>Discount</span><span>$29.80</span></div>
      <div class="calc"><span>Price Per Video</span><span>$119.20</span></div>
      <div class="calc grand"><span>Grand Total</span><span>$119.20</span></div>
      <span class="buy">BUY NOW</span>
    </div>

    <div class="plan plan--featured">
      <div class="plan-head"><span class="plan-name">SUBSCRIPTION</span><span class="plan-sub">NEW VIDEO ADS MONTHLY</span></div>
      <div class="plan-price">STARTS AT ONLY<strong>$16.00</strong>VIDEO FORMAT</div>
      <div class="row">Custom</div><div class="row keep">Starts @ $16/video</div><div class="row">24 hours</div><div class="row">Unlimited</div><div class="row keep">Mp4 FULL HD 1080P</div><div class="row">Included</div><div class="row">Included</div><div class="row">Included</div><div class="row">Included</div><div class="row">Included</div><div class="row">Included</div><div class="row">Included</div><div class="row">Included</div><div class="row">Included</div><div class="row">Included</div><div class="row">Included</div><div class="row">Included</div><div class="row">Included</div><div class="row">Included</div><div class="row">Included</div>
      <div class="qty"><span>-</span><span>1</span><span>+</span></div>
      <div class="calc"><span>Total</span><span>$99</span></div>
      <div class="calc"><span>Discount</span><span>$19.80</span></div>
      <div class="calc"><span>Price Per Video</span><span>$79.20</span></div>
      <div class="calc grand"><span>Grand Total</span><span>$79.20</span></div>
      <span class="buy">BUY NOW</span>
    </div>

    <div class="plan">
      <div class="plan-head"><span class="plan-name">HOLIDAY PKG</span><span class="plan-sub">17 HOLIDAY THEMED VIDEOS</span></div>
      <div class="plan-price">ONLY<strong>$14.00</strong>VIDEO FORMAT</div>
      <div class="row">17</div><div class="row keep">$14/video</div><div class="row">3-5 days</div><div class="row">Unlimited</div><div class="row keep">Mp4 FULL HD 1080P</div><div class="row">Included</div><div class="row">Included</div><div class="row">Included</div><div class="row">Included</div><div class="row">Included</div><div class="row">Not included</div><div class="row">Included</div><div class="row">Included</div><div class="row">Included</div><div class="row">Included</div><div class="row">Included</div><div class="row">Included</div><div class="row">Included</div><div class="row">Included</div><div class="row">Included</div>
      <span class="buy">BUY NOW</span>
    </div>

    <div class="plan">
      <div class="plan-head"><span class="plan-name">SEASON PKG</span><span class="plan-sub">4 SEASONAL THEMED VIDEOS</span></div>
      <div class="plan-price">ONLY<strong>$18.00</strong>VIDEO FORMAT</div>
      <div class="row">4</div><div class="row keep">$18/video</div><div class="row">3-5 days</div><div class="row">Unlimited</div><div class="row keep">Mp4 FULL HD 1080P</div><div class="row">Included</div><div class="row">Included</div><div class="row">Included</div><div class="row">Included</div><div class="row">Not included</div><div class="row">Included</div><div class="row">Included</div><div class="row">Included</div><div class="row">Included</div><div class="row">Included</div><div class="row">Included</div><div class="row">Included</div><div class="row">Included</div><div class="row">Included</div><div class="row">Included</div>
      <span class="buy">BUY NOW</span>
    </div>

    <div class="plan">
      <div class="plan-head"><span class="plan-name">SOCIAL MEDIA</span><span class="plan-sub">DAILY VIDEOS FOR YOUR SOCIAL MEDIA</span></div>
      <div class="plan-price" style="font-weight:700">ONLY<strong>$10.00</strong>VIDEO FORMAT</div>
      <div class="row">30</div><div class="row keep">$10/video</div><div class="row">Prior to next month</div><div class="row">Unlimited</div><div class="row keep">Mp4 FULL HD 1080P</div><div class="row">Not included</div><div class="row">Included</div><div class="row">Not included</div><div class="row">Not included</div><div class="row">Not included</div><div class="row">Included</div><div class="row">Included</div><div class="row">Included</div><div class="row">Included</div><div class="row">Included</div><div class="row">Included</div><div class="row">Included</div><div class="row">Included</div><div class="row">Included</div><div class="row">Included</div>
      <span class="buy">BUY NOW</span>
    </div>
  </section>

  <footer class="site-footer">
    <div class="brand footer-brand"><span class="brand-name">SURGE</span><span class="brand-tag">MARKETING VIDEOS MADE FOR YOU</span></div>
    <p class="footer-tagline">CREATED BY A MARKETER FOR MARKETERS.</p>
    <h2 class="footer-col-title quick-title">Quick Links</h2>
    <ul class="quick-links"><li>How It Works</li><li>Term Of Service</li><li>Privacy Policy</li><li>Cookies Policy</li></ul>
    <h2 class="footer-col-title about-title">About Us</h2>
    <p class="about-text">With Surge, you simply let us know what you want to promote and we will have your video ad finished as soon as 24 hours!</p>
    <div class="social"><span></span><span></span><span></span><span></span><span></span></div>
  </footer>
</div>
</body>
</html>
```